Karvel Wordcraft web design: a translation company with corporate clients

Need a new website for my translation and localization company with file uploading capacity directed to email for quotation

old (very old) web site is www.tpxyazilar.com you can use the content text there or lorem ipsum, We will provide the texts. It will be in English - Turkish - French and German
For the content and overall layout: https://www.plomvinlanguage.com/

For the color scheme you'll need to see logo's colors.

I am rebranding so new logo is uploaded The new adress will be www.karvelwordcraft.com

Target Market(s)

Primarily corporate clients

Industry/Entity Type

It Company

Coding

Coded - Design and coding required

Number of Pages Required

5+ page

Font styles to use
Other font styles liked:
• Calibri

Requirements
Must have
• References on homepage (logos will be sent during design phase)
• Services: Translation, Interpretation, Localization&Consultancy, Translation API
• Quotation Form and file uploading
• Simple layout evoking reliability, speed and accuracy
Nice to have
• For the content and overall layout: https://www.plomvinlanguage.com/
• Separate page for Translation Services: Marketing Translation, Legal Translation, Technical Translation, Personal Translation
• and texts under these headings
Should not have
• Old style
• Complex design

```html
<!DOCTYPE html>
<html lang="en">
<head>
<meta charset="utf-8">
<title>Karvel Wordcraft — Translation, Localization &amp; Consultancy</title>
<link rel="stylesheet" href="https://fonts.googleapis.com/css2?family=Roboto+Condensed:wght@400;700&family=Open+Sans:ital,wght@0,400;0,600;1,400&display=swap">
<style>
:root{
  --orange:#e39530;
  --orange-deep:#d6841f;
  --olive:#5d6c38;
  --olive-dark:#4e5d31;
  --olive-text:#4c5630;
  --teal:#21b59b;
  --coral:#f26b2b;
  --ink:#333;
  --muted:#666;
  --light:#f2f2f2;
  --line:#dcdcdc;
  --white:#fff;
}
*{box-sizing:border-box;margin:0;padding:0}
html,body{width:1200px;height:2575px;overflow:hidden}
body{font-family:"Open Sans",Arial,sans-serif;color:var(--ink);background:var(--white);position:relative}
.abs{position:absolute}
ul{list-style:none}

/* top bar */
.topbar{top:0;left:0;width:1200px;height:34px;background:var(--orange);color:var(--white);font-size:12px}
.topbar .contact{position:absolute;top:10px;left:390px;display:flex;gap:40px}
.topbar .langs{position:absolute;top:10px;left:778px;display:flex;gap:18px}
.topbar .langs span{display:flex;align-items:center;gap:5px}
.flag{width:16px;height:11px;display:inline-block;background:var(--white);opacity:.85}
.topbar svg{vertical-align:-2px;margin-right:6px}

/* header */
.header{top:34px;left:0;width:1200px;height:100px;background:var(--white);box-shadow:0 1px 3px rgba(0,0,0,.08)}
.brand{position:absolute;left:98px;top:33px;display:flex;align-items:center;gap:10px;font-family:"Roboto Condensed",Arial,sans-serif;font-size:25px;color:var(--olive-text)}
.brand .dot{width:14px;height:14px;border-radius:50%;background:var(--orange)}
.nav{position:absolute;top:48px;left:375px;display:flex;gap:44px;font-family:"Roboto Condensed",Arial,sans-serif;font-size:13.5px;color:#333;text-transform:uppercase}
.nav .active{color:var(--orange)}

/* hero */
.hero{top:134px;left:0;width:1200px;height:515px;background:linear-gradient(100deg,#eef0f1 0%,#e4e7e9 40%,#b9c2c9 70%,#8d99a3 100%)}
.hero h1{position:absolute;left:100px;top:143px;font-family:"Roboto Condensed",Arial,sans-serif;font-weight:700;font-size:33px;line-height:43px;color:var(--olive-text);text-transform:uppercase}
.hero ul{position:absolute;left:100px;top:240px;font-size:14px;color:#333}
.hero li{height:29px;display:flex;align-items:center;gap:14px}
.hero li i{width:11px;height:11px;border-radius:50%;background:#444;position:relative}
.hero li i::after{content:"";position:absolute;left:3px;top:3px;border-left:5px solid #fff;border-top:2.5px solid transparent;border-bottom:2.5px solid transparent}
.btn-more{position:absolute;left:100px;top:366px;width:135px;height:40px;background:var(--orange);color:#fff;font-size:14px;display:flex;align-items:center;justify-content:center;gap:6px;border-radius:2px}
.hero .arrow{position:absolute;top:238px;width:14px;height:14px;border-left:2px solid rgba(255,255,255,.8);border-bottom:2px solid rgba(255,255,255,.8)}

/* clients */
.clients{top:649px;left:0;width:1200px;height:101px;background:var(--light);display:flex;justify-content:center;align-items:center;gap:70px;font-family:"Open Sans",Arial,sans-serif;font-weight:600;font-size:22px;color:#4a4a4a}
.clients span{display:flex;align-items:center;gap:8px}
.clients i{width:16px;height:16px;background:#8a8a8a;display:inline-block}

/* section titles */
.section-title{font-family:"Roboto Condensed",Arial,sans-serif;font-weight:400;font-size:32px;color:var(--olive-text);text-align:center;width:1200px}

/* services */
.services-title{top:822px;left:0}
.service{top:932px;width:240px;text-align:center}
.service .icon{width:113px;height:113px;border-radius:50%;margin:0 auto;display:flex;align-items:center;justify-content:center}
.service h3{margin-top:25px;font-family:"Roboto Condensed",Arial,sans-serif;font-weight:400;font-size:16px;color:#333;text-transform:uppercase}
.service p{margin-top:6px;font-size:11.5px;line-height:19px;color:var(--muted)}
.service .chev{margin-top:18px}

/* orange band */
.band{top:1231px;left:0;width:1200px;height:623px;background:linear-gradient(180deg,#e39a39,#dc8b27)}
.card{position:absolute;background:var(--white);border-radius:3px;box-shadow:0 2px 6px rgba(0,0,0,.15)}
.quote-card{left:98px;top:1286px;width:530px;height:515px}
.quote-card h2{text-align:center;margin-top:22px;font-family:"Roboto Condensed",Arial,sans-serif;font-weight:400;font-size:30px;color:var(--olive-text)}
.field-label{position:absolute;left:22px;font-size:13px;color:#444}
.select{position:absolute;left:22px;width:484px;height:38px;border:1px solid var(--line);border-radius:2px;display:flex;align-items:center;font-size:11px;color:#555}
.select .ico{width:40px;height:100%;border-right:1px solid var(--line);display:flex;align-items:center;justify-content:center;margin-right:14px}
.select .caret{position:absolute;right:12px;top:16px;border-top:5px solid #444;border-left:4px solid transparent;border-right:4px solid transparent}
.listbox{position:absolute;top:323px;height:124px;border:1px solid var(--line);font-size:11px;color:#666;line-height:18px;padding:6px 10px}
.listbox .bar{position:absolute;right:0;top:0;width:12px;height:100%;border-left:1px solid var(--line);background:#f7f7f7}
.swap{position:absolute;left:258px;top:375px;font-size:13px;color:#555}
.btn-next{position:absolute;left:417px;top:465px;width:89px;height:35px;background:var(--olive);color:#fff;font-size:13px;display:flex;align-items:center;justify-content:center;border-radius:2px}

.news-card{left:656px;top:1286px;width:444px;height:515px}
.news-card h2{position:absolute;left:24px;top:26px;font-family:"Roboto Condensed",Arial,sans-serif;font-weight:400;font-size:20px;color:#333}
.news-item{position:absolute;left:24px;width:400px;height:115px}
.news-item .thumb{position:absolute;left:0;top:0;width:124px;height:115px}
.news-item .body{position:absolute;left:146px;top:0;width:250px}
.news-item h4{font-family:"Roboto Condensed",Arial,sans-serif;font-weight:400;font-size:15px;color:var(--olive-text)}
.news-item .meta{margin-top:8px;font-size:10px;color:#444}
.news-item p{margin-top:8px;font-size:10.5px;line-height:19px;color:#555}

/* reviews */
.reviews{top:1854px;left:0;width:1200px;height:373px;background:var(--light)}
.reviews-title{top:1937px;left:0}
.review{position:absolute;top:2043px;width:500px}
.review .avatar{position:absolute;left:0;top:0;width:120px;height:120px;border-radius:50%;border:4px solid #fff;background:linear-gradient(180deg,#d9dde1,#4a5666);box-shadow:0 1px 3px rgba(0,0,0,.15)}
.review .text{position:absolute;left:138px;top:8px;width:370px;font-style:italic;font-size:11px;line-height:20.5px;color:#555}
.review .text::before{content:"\201C";font-size:22px;color:#999;margin-right:3px;vertical-align:-6px}
.stars{margin-top:2px;color:var(--orange);font-size:11px;font-style:normal;letter-spacing:1px}
.stars b{color:#ccc;font-weight:400}
.review .name{margin-top:4px;font-size:12px;color:#666}

/* footer */
.footer{top:2227px;left:0;width:1200px;height:295px;background:var(--olive-dark);color:#fff}
.footer h5{font-family:"Roboto Condensed",Arial,sans-serif;font-weight:400;font-size:17px;text-transform:uppercase;margin-bottom:22px}
.fcol{position:absolute;top:50px;font-size:12px;line-height:18px}
.frow{display:flex;gap:16px;margin-bottom:18px}
.frow svg{flex:none;margin-top:2px}
.tweet{display:flex;gap:16px;margin-bottom:18px}
.tweet .tw{flex:none;width:14px;height:14px;background:#fff;border-radius:2px;margin-top:3px}
.tweet small{display:block;margin-top:6px;font-size:11px}
.news-input{width:243px;height:40px;background:#fff;color:#444;font-size:11px;display:flex;align-items:center;padding-left:14px;margin-top:16px}
.subscribe-row{display:flex;align-items:center;gap:20px;margin-top:16px}
.btn-sub{width:102px;height:38px;background:var(--orange);display:flex;align-items:center;justify-content:center;font-size:12px;text-transform:uppercase}
.social{display:flex;gap:6px}
.social i{width:24px;height:24px;border-radius:50%;background:#fff;display:inline-block}
.quick li{line-height:24px}

.copyright{top:2522px;left:0;width:1200px;height:53px;background:var(--orange);color:#fff;font-size:12px;display:flex;align-items:center;justify-content:center}
</style>
</head>
<body>

<div class="abs topbar">
  <div class="contact">
    <span><svg width="12" height="12" viewBox="0 0 24 24" fill="#fff"><path d="M6.6 10.8a15.1 15.1 0 0 0 6.6 6.6l2.2-2.2a1 1 0 0 1 1-.25 11.4 11.4 0 0 0 3.6.57 1 1 0 0 1 1 1V20a1 1 0 0 1-1 1A17 17 0 0 1 3 4a1 1 0 0 1 1-1h3.5a1 1 0 0 1 1 1c0 1.25.2 2.45.57 3.57a1 1 0 0 1-.25 1z"/></svg>+0 216 407 3150</span>
    <span><svg width="14" height="11" viewBox="0 0 24 18" fill="none" stroke="#fff" stroke-width="2"><rect x="1" y="1" width="22" height="16"/><path d="M1 1l11 9 11-9"/></svg>Email: info@tpxyazilar.com</span>
  </div>
  <div class="langs">
    <span><i class="flag"></i>English</span>
    <span><i class="flag"></i>Turkish</span>
    <span><i class="flag"></i>Turkish</span>
    <span><i class="flag"></i>German</span>
  </div>
</div>

<header class="abs header">
  <div class="brand"><span class="dot"></span>Karvel Wordcraft</div>
  <nav class="nav">
    <span class="active">Home</span>
    <span>Translation Services</span>
    <span>Online Translation</span>
    <span>References</span>
    <span>About Us</span>
    <span>Contact</span>
  </nav>
</header>

<section class="abs hero" role="img" aria-label="Photo of three smiling colleagues working together around a laptop in a bright office">
  <h1>Delivery on time with<br>perfect quality</h1>
  <ul>
    <li><i></i>Translation</li>
    <li><i></i>Interpretation</li>
    <li><i></i>Localization&amp;Consultancy</li>
    <li><i></i>Translation API</li>
  </ul>
  <div class="btn-more">MORE INFO <svg width="12" height="12" viewBox="0 0 12 12"><circle cx="6" cy="6" r="6" fill="#fff"/><path d="M5 3.5L7.5 6 5 8.5" stroke="#e39530" stroke-width="1.6" fill="none"/></svg></div>
  <span class="arrow" style="left:30px;transform:rotate(45deg)"></span>
  <span class="arrow" style="left:1150px;transform:rotate(-135deg)"></span>
</section>

<section class="abs clients" aria-label="References">
  <span><i></i>Voltara</span>
  <span><i></i>NORU</span>
  <span><i></i>Harlow &amp; Finch</span>
  <span><i></i>quillbase</span>
  <span><i></i>Ostmark Media</span>
</section>

<h2 class="abs section-title services-title">Translation Services</h2>

<div class="abs service" style="left:84px">
  <div class="icon" style="background:var(--orange)"><svg width="48" height="48" viewBox="0 0 48 48" fill="#fff"><path d="M8 14h10a5 5 0 1 1 10 0h10v10a5 5 0 1 1 0 10v10H28a5 5 0 1 0-10 0H8V34a5 5 0 1 0 0-10z"/></svg></div>
  <h3>Marketing Translation</h3>
  <p>Nemo enim ipsam voluptatem quia volut sit aspernatur aut odit aut fugit, sed quia consequuntur magni dolores</p>
  <svg class="chev" width="14" height="12" viewBox="0 0 14 12" fill="none" stroke="#333" stroke-width="1.5"><path d="M2 1l5 4 5-4M2 6l5 4 5-4"/></svg>
</div>
<div class="abs service" style="left:350px">
  <div class="icon" style="background:var(--olive)"><svg width="48" height="48" viewBox="0 0 48 48" fill="#fff"><rect x="14" y="8" width="14" height="22" rx="2" transform="rotate(-45 21 19)"/><rect x="22" y="22" width="6" height="24" rx="2" transform="rotate(-45 25 34)"/></svg></div>
  <h3>Legal Translation</h3>
  <p>Nemo enim ipsam voluptatem quia volut sit aspernatur aut odit aut fugit, sed quia consequuntur magni dolores</p>
  <svg class="chev" width="14" height="12" viewBox="0 0 14 12" fill="none" stroke="#333" stroke-width="1.5"><path d="M2 1l5 4 5-4M2 6l5 4 5-4"/></svg>
</div>
<div class="abs service" style="left:615px">
  <div class="icon" style="background:var(--teal)"><svg width="50" height="50" viewBox="0 0 50 50" fill="none" stroke="#fff"><circle cx="20" cy="28" r="8" stroke-width="6" stroke-dasharray="4 2.3"/><circle cx="20" cy="28" r="3" fill="#fff" stroke="none"/><circle cx="36" cy="14" r="6" stroke-width="4" stroke-dasharray="3 2"/></svg></div>
  <h3>Technical Translation</h3>
  <p>Nemo enim ipsam voluptatem quia volut sit aspernatur aut odit aut fugit, sed quia consequuntur magni dolores</p>
  <svg class="chev" width="14" height="12" viewBox="0 0 14 12" fill="none" stroke="#333" stroke-width="1.5"><path d="M2 1l5 4 5-4M2 6l5 4 5-4"/></svg>
</div>
<div class="abs service" style="left:872px">
  <div class="icon" style="background:var(--coral)"><svg width="44" height="44" viewBox="0 0 44 44" fill="#fff"><circle cx="22" cy="14" r="9"/><path d="M6 40c0-9 7-15 16-15s16 6 16 15z"/></svg></div>
  <h3>Personal Translation</h3>
  <p>Nemo enim ipsam voluptatem quia volut sit aspernatur aut odit aut fugit, sed quia consequuntur magni dolores</p>
  <svg class="chev" width="14" height="12" viewBox="0 0 14 12" fill="none" stroke="#333" stroke-width="1.5"><path d="M2 1l5 4 5-4M2 6l5 4 5-4"/></svg>
</div>

<section class="abs band" role="img" aria-label="Faint city skyline photo tinted orange behind the form and news panels"></section>

<div class="card quote-card">
  <h2>Online Translation</h2>
  <span class="field-label" style="top:72px">Timeframe :</span>
  <div class="select" style="top:92px"><span class="ico"><svg width="12" height="12" viewBox="0 0 12 12" fill="none" stroke="#666" stroke-width="1.3"><circle cx="6" cy="6" r="5"/><path d="M6 3v3l2 1"/></svg></span>Express (within 48 hours)<i class="caret"></i></div>
  <span class="field-label" style="top:150px">Certification :</span>
  <div class="select" style="top:170px"><span class="ico"><svg width="11" height="13" viewBox="0 0 11 13" fill="#666"><path d="M5.5 0L11 2v4c0 3.5-2.4 6-5.5 7C2.4 12 0 9.5 0 6V2z"/></svg></span>Not Required<i class="caret"></i></div>
  <span class="field-label" style="top:227px">Translate from :</span>
  <div class="select" style="top:247px"><span class="ico"><svg width="12" height="12" viewBox="0 0 12 12"><circle cx="6" cy="6" r="6" fill="#666"/></svg></span>English<i class="caret"></i></div>
  <span class="field-label" style="top:305px">Translate To :</span>
  <div class="listbox" style="left:22px;width:218px">Arabic<br>English<br>English (USA)<br>Esperanto<br>Estonian<br>Faroese<span class="bar"></span></div>
  <span class="swap">⇄</span>
  <div class="listbox" style="left:290px;width:216px"><span class="bar"></span></div>
  <div class="btn-next">NEXT »</div>
</div>

<div class="card news-card">
  <h2>LATEST NEWS</h2>
  <div class="news-item" style="top:74px">
    <div class="thumb" role="img" aria-label="Photo of a person working at a desk with a computer" style="background:linear-gradient(135deg,#8fa2b4,#3f4c5a)"></div>
    <div class="body"><h4>Nemo Enim Ipsam Voluptatem</h4><div class="meta">3 MINUTES AGO &nbsp; / &nbsp; 0 COMMENTS</div><p>Lorem ipsum dolor sit amet, consectetur scing elit, sed do eiusmod tempor incididunt ut labore et dolore magna aliqua.</p></div>
  </div>
  <div class="news-item" style="top:221px">
    <div class="thumb" role="img" aria-label="Photo of hands arranging colourful notes on a table" style="background:linear-gradient(135deg,#3aa5a0,#e07a3c)"></div>
    <div class="body"><h4>Nemo Enim Ipsam Voluptatem</h4><div class="meta">3 MINUTES AGO &nbsp; / &nbsp; 0 COMMENTS</div><p>Lorem ipsum dolor sit amet, consectetur scing elit, sed do eiusmod tempor incididunt ut labore et dolore magna aliqua.</p></div>
  </div>
  <div class="news-item" style="top:368px">
    <div class="thumb" role="img" aria-label="Top-down photo of a team meeting around a white table" style="background:linear-gradient(135deg,#2d3440,#b8bcc2)"></div>
    <div class="body"><h4>Nemo Enim Ipsam Voluptatem</h4><div class="meta">3 MINUTES AGO &nbsp; / &nbsp; 0 COMMENTS</div><p>Lorem ipsum dolor sit amet, consectetur scing elit, sed do eiusmod tempor incididunt ut labore et dolore magna aliqua.</p></div>
  </div>
</div>

<section class="abs reviews"></section>
<h2 class="abs section-title reviews-title">Customer Reviews</h2>

<div class="review" style="left:98px">
  <div class="avatar" role="img" aria-label="Portrait photo of a customer in a suit"></div>
  <div class="text">You should know that you have designed a very robust and adaptable system, when we started discussing our needs turnover and volumes were around half of what we are handling today.
    <div class="stars">★★★<b>★★</b></div>
    <div class="name">JOHN DOE</div></div>
</div>
<div class="review" style="left:640px">
  <div class="avatar" role="img" aria-label="Portrait photo of a customer in a suit"></div>
  <div class="text">You should know that you have designed a very robust and adaptable system, when we started discussing our needs turnover and volumes were around half of what we are handling today.
    <div class="stars">★★★<b>★★</b></div>
    <div class="name">JOHN DOE</div></div>
</div>

<footer class="abs footer">
  <div class="fcol" style="left:98px;width:260px">
    <h5>Contact Us</h5>
    <div class="frow"><svg width="14" height="18" viewBox="0 0 14 18" fill="none" stroke="#fff" stroke-width="1.4"><path d="M7 17s6-6 6-10A6 6 0 0 0 1 7c0 4 6 10 6 10z"/><circle cx="7" cy="7" r="2"/></svg><span>Lale Sok. Serin Apt.<br>No. 12 Daire 3 Yeşilköy, 34149<br>Bakırköy-İstanbul</span></div>
    <div class="frow"><svg width="14" height="14" viewBox="0 0 24 24" fill="none" stroke="#fff" stroke-width="1.8"><path d="M6.6 10.8a15.1 15.1 0 0 0 6.6 6.6l2.2-2.2 4.6 1V20A17 17 0 0 1 3 4h4.3l1 4.6z"/></svg><span>Phone : 0 216 407 3150</span></div>
    <div class="frow"><svg width="16" height="12" viewBox="0 0 24 18" fill="none" stroke="#fff" stroke-width="2"><rect x="1" y="1" width="22" height="16"/><path d="M1 1l11 9 11-9"/></svg><span>info@tpxyazilar.com</span></div>
  </div>
  <div class="fcol" style="left:386px;width:270px">
    <h5>Latest Tweet`s</h5>
    <div class="tweet"><i class="tw"></i><div><b>@Karvel.</b> Fusce susct varius mi. Cum sociis natoque penabus et<small>1 day ago</small></div></div>
    <div class="tweet"><i class="tw"></i><div><b>@Karvel.</b> Fusce susct varius mi. Cum sociis natoque penabus et<small>1 day ago</small></div></div>
  </div>
  <div class="fcol" style="left:692px;width:260px">
    <h5>Join Our Newsletter</h5>
    <p style="margin-top:-6px">Excepteur sint occaecat cupidatat non proident, sunt in culpa qui</p>
    <div class="news-input">Enter Name</div>
    <div class="subscribe-row"><span class="btn-sub">Subscribe</span><span class="social"><i></i><i></i><i></i><i></i></span></div>
  </div>
  <div class="fcol" style="left:998px;width:150px">
    <h5>Quick Links</h5>
    <ul class="quick" style="margin-top:-4px">
      <li>Home</li><li>Our Services</li><li>Online Translation</li><li>Graphics Design</li><li>References</li><li>Contact Us</li>
    </ul>
  </div>
</footer>

<div class="abs copyright">Copyright 2016 | All Rights Reserved – Karvel Wordcraft</div>

</body>
</html>
```